Zirkus Design (Hintergrund)
Zielgruppe
Familien, Eltern, Kinder (Jugendliche), LehrerInnen / Pädagogen, päd. Einrichtungen, Firmen
kreativ, künstlerisch, welt offen, international, sozial, engagiert, sportlich
Aufgabenstellung
Das Layout soll multifunktional sein, das heist in seinen Grundzügen oder leicht abgewandelt soll es für Postkarten, Flyer (DIN A 4 3 fach geknickt) und evtl. Plakate (als Hintergrund) Verwendung finden.
Und es soll für verschiedene Projekte / Veranstaltungen wiederverwendet werden, da ich nicht das Budget habe jedesmal ein neues Layout machen zu lassen.

```html
<!DOCTYPE html>
<html lang="de">
<head>
<meta charset="utf-8">
<title>Zirkus – Hintergrund-Layout</title>
<link rel="stylesheet" href="https://fonts.googleapis.com/css2?family=PT+Sans:wght@400;700&display=swap">
<style>
  :root {
    --page: #f2f2f0;
    --cream: #fcf6e6;
    --ray: #f7e4b8;
    --red: #c13b30;
    --green: #8dc24c;
    --ink: #3a3a3a;
    --fold: #b9b1a0;
  }
  * { margin: 0; padding: 0; box-sizing: border-box; }
  html, body { width: 1200px; height: 900px; overflow: hidden; background: var(--page); }
  body { position: relative; font-family: "PT Sans", sans-serif; color: var(--ink); }

  .sheet {
    position: absolute;
    overflow: hidden;
    background: var(--cream);
    box-shadow: 0 2px 10px rgba(0,0,0,.12);
  }
  .sheet__rays {
    position: absolute; inset: 0;
    background: radial-gradient(ellipse 90% 110% at 50% 100%, var(--ray) 0%, var(--cream) 75%);
  }
  .sheet__art { position: absolute; inset: 0; width: 100%; height: 100%; }

  .spread { width: 560px; height: 396px; left: 40px; }
  .spread--inside { top: 30px; }
  .spread--outside { top: 474px; }
  .card { width: 240px; height: 508px; top: 196px; }
  .card--first { left: 660px; }
  .card--second { left: 920px; }

  .brand {
    position: absolute;
    display: flex; align-items: center; gap: 4px;
    color: var(--red);
    font-weight: 700;
    white-space: nowrap;
  }
  .brand__dot { width: 7px; height: 7px; border-radius: 50%; background: var(--red); flex: none; }
  .brand--cover { left: 478px; top: 84px; font-size: 13px; }
  .brand--contact { left: 232px; top: 268px; font-size: 12px; }
  .brand--card { left: 22px; top: 108px; font-size: 20px; }
  .brand--card .brand__dot { width: 10px; height: 10px; }

  .contact {
    position: absolute; left: 232px; top: 290px;
    font-size: 7.5px; line-height: 1.35;
  }
  .contact p + p { margin-top: 5px; }
</style>
</head>
<body>

<!-- Innenseite, dreifach gefalzt -->
<section class="sheet spread spread--inside">
  <div class="sheet__rays" role="img" aria-label="Cremefarbener Strahlenkranz-Hintergrund"></div>
  <svg class="sheet__art" viewBox="0 0 560 396">
    <rect x="0" y="30" width="560" height="16" fill="var(--red)"/>
    <g fill="none" stroke="var(--cream)" stroke-width="2">
      <circle cx="12" cy="42" r="6"/><circle cx="28" cy="33" r="8"/>
      <circle cx="199" cy="42" r="6"/><circle cx="215" cy="33" r="8"/>
      <circle cx="385" cy="42" r="6"/><circle cx="401" cy="33" r="8"/>
    </g>
    <line x1="186.7" y1="0" x2="186.7" y2="396" stroke="var(--fold)" stroke-dasharray="4 3" stroke-width=".7"/>
    <line x1="373.3" y1="0" x2="373.3" y2="396" stroke="var(--fold)" stroke-dasharray="4 3" stroke-width=".7"/>
    <rect x="0" y="378" width="560" height="18" fill="var(--green)"/>
    <g fill="none" stroke="var(--green)" stroke-width="2">
      <circle cx="8" cy="372" r="6"/><circle cx="28" cy="366" r="10"/>
    </g>
  </svg>
</section>

<!-- Außenseite mit Titel und Kontakt -->
<section class="sheet spread spread--outside">
  <div class="sheet__rays" role="img" aria-label="Cremefarbener Strahlenkranz-Hintergrund"></div>
  <svg class="sheet__art" viewBox="0 0 560 396">
    <rect x="0" y="30" width="560" height="16" fill="var(--red)"/>
    <g fill="none" stroke="var(--cream)" stroke-width="2">
      <circle cx="12" cy="42" r="6"/><circle cx="28" cy="33" r="8"/>
      <circle cx="199" cy="42" r="6"/><circle cx="215" cy="33" r="8"/>
      <circle cx="385" cy="42" r="6"/><circle cx="401" cy="33" r="8"/>
    </g>
    <line x1="186.7" y1="0" x2="186.7" y2="396" stroke="var(--fold)" stroke-dasharray="4 3" stroke-width=".7"/>
    <line x1="373.3" y1="0" x2="373.3" y2="396" stroke="var(--fold)" stroke-dasharray="4 3" stroke-width=".7"/>
    <circle cx="415" cy="305" r="42" fill="none" stroke="var(--red)" stroke-width="9"/>
    <circle cx="548" cy="225" r="55" fill="none" stroke="var(--green)" stroke-width="8"/>
    <rect x="0" y="378" width="560" height="18" fill="var(--green)"/>
    <g fill="none" stroke="var(--green)" stroke-width="2">
      <circle cx="8" cy="372" r="6"/><circle cx="28" cy="366" r="10"/>
    </g>
  </svg>
  <div class="brand brand--cover"><span class="brand__dot"></span>Zirkus Jonte Brask</div>
  <div class="brand brand--contact"><span class="brand__dot"></span>Zirkus Jonte Brask</div>
  <address class="contact">
    <p>Lena Roswald<br>Zeltgasse 7<br>54321 Manegenfeld</p>
    <p>Telefon (123 45) 12 34 56<br>Telefax (123 45) 12 34 56</p>
    <p>post@zeltwerk-mail.de<br>www.zeltwerk-seite.de</p>
  </address>
</section>

<!-- Postkarten / Einleger -->
<section class="sheet card card--first">
  <div class="sheet__rays" role="img" aria-label="Cremefarbener Strahlenkranz-Hintergrund"></div>
  <svg class="sheet__art" viewBox="0 0 240 508">
    <rect x="0" y="38" width="240" height="20" fill="var(--red)"/>
    <g fill="none" stroke="var(--cream)" stroke-width="2">
      <circle cx="14" cy="54" r="7"/><circle cx="34" cy="42" r="10"/>
    </g>
    <circle cx="240" cy="245" r="70" fill="none" stroke="var(--green)" stroke-width="10"/>
    <circle cx="45" cy="385" r="48" fill="none" stroke="var(--red)" stroke-width="12"/>
    <rect x="0" y="486" width="240" height="22" fill="var(--green)"/>
  </svg>
  <div class="brand brand--card"><span class="brand__dot"></span>Zirkus Jonte Brask</div>
</section>

<section class="sheet card card--second">
  <div class="sheet__rays" role="img" aria-label="Cremefarbener Strahlenkranz-Hintergrund"></div>
  <svg class="sheet__art" viewBox="0 0 240 508">
    <rect x="0" y="38" width="240" height="20" fill="var(--red)"/>
    <g fill="none" stroke="var(--cream)" stroke-width="2">
      <circle cx="14" cy="54" r="7"/><circle cx="34" cy="42" r="10"/>
    </g>
    <circle cx="240" cy="245" r="70" fill="none" stroke="var(--green)" stroke-width="10"/>
    <circle cx="45" cy="385" r="48" fill="none" stroke="var(--red)" stroke-width="12"/>
    <rect x="0" y="486" width="240" height="22" fill="var(--green)"/>
  </svg>
  <div class="brand brand--card"><span class="brand__dot"></span>Zirkus Jonte Brask</div>
</section>

</body>
</html>
```